Web Design for UK Based Technology Company*

Korvane is a new entrant in the data marketplace.
It is offering two direct API services to help clients access:
- Company Data
- Location Data
We also offer data services and consulting to help companies to integrate our API services and the data derived from them into their businesses. Our aim is to offer both the technology and services to help businesses use and integrate data better. It is a modern business built to support a modern world.

Target Market(s)

Business Professionals and decision makers

Industry/Entity Type

It Service

Number of Pages Required

5+ page

Font styles to use
Sans Serif

Colors

Designer to choose colors to be used in the design.

Requirements
Must have
• The full suite of PSD designs taking into account the layouts and wireframes supplied with which it will be compared. Focus on the homepage first. It has to have a consistent theme/feel. It has to fit with the logo.
Nice to have
• Simple, clean, a few strong ideas.
Should not have
• Cartoons, overdesign, loud colours.

```html
<!DOCTYPE html>
<html lang="en">
<head>
<meta charset="utf-8">
<title>Korvane – Richer Data To Drive Your Business</title>
<link href="https://fonts.googleapis.com/css2?family=Lato:wght@400;700;900&display=swap" rel="stylesheet">
<style>
:root{
  --blue:#1e8fe1;
  --navy:#1b4f9d;
  --navy-deep:#163f80;
  --ink:#333a44;
  --muted:#5c636d;
  --footer:#1f5aa8;
  --white:#fff;
  --line:#e6e9ee;
}
*{box-sizing:border-box;margin:0;padding:0}
html,body{width:1200px;height:3424px;overflow:hidden}
body{font-family:'Lato',sans-serif;color:var(--ink);background:var(--white);position:relative}
.abs{position:absolute}
a{color:inherit;text-decoration:none}

/* top bar + nav */
.topbar{top:0;left:0;width:1200px;height:27px;border-bottom:1px solid var(--line);font-size:9px;color:#8a9099;display:flex;justify-content:flex-end;align-items:center;gap:22px;padding-right:150px;letter-spacing:.3px}
.topbar span{display:flex;align-items:center;gap:6px}
.nav{top:27px;left:0;width:1200px;height:65px}
.brand{left:150px;top:18px;font-weight:900;font-size:20px;color:var(--navy-deep);display:flex;align-items:center;gap:8px;letter-spacing:.3px}
.brand i{width:16px;height:16px;background:var(--blue);display:block}
.nav-link{top:25px;font-size:11px;letter-spacing:.8px;color:#4a515b}
.nav-link.active{color:var(--blue)}
.btn{display:flex;align-items:center;justify-content:center;font-size:11px;font-weight:700;letter-spacing:.6px;border-radius:2px}
.btn-solid{background:var(--blue);color:var(--white)}
.btn-white{background:var(--white);color:var(--ink);font-weight:400}
.btn-ghost{border:2px solid var(--white);color:var(--white);background:rgba(22,63,128,.55)}
.btn-outline{border:2px solid var(--blue);color:var(--blue);font-weight:400;background:var(--white)}

/* hero */
.hero{top:92px;left:0;width:1200px;height:586px;background:linear-gradient(120deg,#3f6f9f 0%,#5d8fc0 45%,#4a7bb0 75%,#6f9ccc 100%)}
.hero h1{top:100px;width:1200px;text-align:center;font-size:37px;font-weight:400;letter-spacing:3px;color:var(--white)}
.hero .lead{top:164px;width:1200px;text-align:center;font-size:17px;font-weight:700;letter-spacing:1px;color:var(--white)}
.hero-card{background:var(--navy);color:var(--white);padding:26px 52px}
.hero-card h2{font-weight:400;font-size:23px;letter-spacing:1.8px;line-height:31px}
.hero-curve{left:0;top:640px}

/* who we are */
.rule{width:28px;height:4px;background:var(--blue)}
.who h2{font-size:27px;font-weight:700;color:var(--ink)}
.who p{font-size:13.5px;line-height:16px;letter-spacing:.8px;color:var(--muted);text-align:justify}
.who p + p{margin-top:16px}
.who u{color:var(--muted)}
.illustration{left:601px;top:702px;width:449px;height:461px;border-radius:6px;background:linear-gradient(150deg,#eef1f4 0%,#d7e8f4 50%,#eef1f4 100%)}

/* services */
.services{top:1203px;left:0;width:1200px;height:711px;background:linear-gradient(180deg,#2e6ea8 0%,#1f64a8 40%,#1a5ea5 100%)}
.services h2{left:152px;top:42px;font-size:27px;font-weight:700;color:var(--white)}
.service-card{left:246px;width:714px;height:256px;background:rgba(25,70,135,.78);color:var(--white);text-align:center}
.service-card h3{margin-top:34px;font-size:22px;font-weight:700;display:flex;align-items:center;justify-content:center;gap:8px}
.service-card p{margin-top:22px;font-size:14.5px;font-weight:700;line-height:27px;letter-spacing:.8px}
.badge{width:80px;height:80px;top:14px;left:618px}
.badge span{position:absolute;left:0;width:80px;text-align:center;color:var(--white)}

/* cta */
.cta h2{top:1960px;width:1200px;text-align:center;font-size:28px;font-weight:700;color:var(--ink)}
.cta p{top:2030px;left:235px;width:730px;text-align:center;font-size:13px;line-height:16px;letter-spacing:.9px;color:var(--muted)}
.divider{top:2200px;left:0;width:1200px;height:1px;background:var(--line)}

/* demanding */
.photo{left:150px;top:2254px;width:277px;height:306px;background:linear-gradient(160deg,#5a6068,#2b3036 60%,#1c2024)}
.demand h2{left:458px;top:2249px;font-size:27px;font-weight:700;color:#222}
.demand .body{left:459px;top:2316px;width:590px;font-size:13px;line-height:16px;letter-spacing:.9px;color:var(--muted)}
.demand ul{margin:0 0 0 14px;list-style:none}
.demand li::before{content:"●";margin-right:6px;font-size:10px}

/* location */
.map{left:0;top:2629px;width:1200px;height:388px;background:linear-gradient(100deg,#dfe9dc 0%,#e9ece6 35%,#cfe3c9 60%,#e6e9e3 100%)}
.loc-panel{left:150px;top:2629px;width:404px;height:388px;background:rgba(70,70,70,.82);color:var(--white);padding:46px 38px}
.loc-panel h2{font-size:23px;font-weight:700;letter-spacing:1.6px}
.loc-panel address{margin-top:30px;font-style:normal;font-size:14.5px;font-weight:700;line-height:27px}

/* footer */
.footer{top:3017px;left:0;width:1200px;height:407px;background:linear-gradient(135deg,#1c54a2 0%,#2563b2 50%,#1d57a6 100%);color:var(--white)}
.foot-col{top:76px}
.foot-col h4{font-size:17.5px;font-weight:700;margin-bottom:24px}
.foot-col a{display:block;font-size:12px;letter-spacing:1px;height:45px}
.legal{left:0;top:385px;width:1200px;height:22px;background:#8fb7e3;font-size:9px;color:#2a4a7a;display:flex;align-items:center;padding:0 150px}
.legal nav{margin-left:auto;display:flex;gap:30px}
</style>
</head>
<body>

<div class="topbar abs">
  <span>Contact Us</span>
  <span><svg width="9" height="9" viewBox="0 0 24 24"><path fill="#8a9099" d="M6.6 10.8a15 15 0 006.6 6.6l2.2-2.2c.3-.3.7-.4 1-.2 1.1.4 2.3.6 3.6.6.6 0 1 .4 1 1V20c0 .6-.4 1-1 1A17 17 0 013 4c0-.6.4-1 1-1h3.5c.6 0 1 .4 1 1 0 1.3.2 2.5.6 3.6.1.3 0 .7-.2 1z"/></svg>(+44) 01632 960 214</span>
  <span><svg width="9" height="8" viewBox="0 0 24 20"><path fill="#8a9099" d="M0 0h24v20H0zM2 2l10 8 10-8"/></svg>hello@korvane-data.example</span>
</div>

<header class="nav abs">
  <a class="brand abs"><i></i>KORVANE</a>
  <a class="nav-link abs" style="left:299px">Company Data</a>
  <a class="nav-link abs active" style="left:412px">Location Data</a>
  <a class="nav-link abs" style="left:522px">Services</a>
  <a class="nav-link abs" style="left:600px">About Us</a>
  <a class="nav-link abs" style="left:876px">Login</a>
  <a class="btn btn-solid abs" style="left:937px;top:13px;width:113px;height:36px">Free Trail</a>
</header>

<section class="hero abs" role="img" aria-label="Photo of a desk with a hand writing on newspapers, a laptop and a coffee cup, tinted blue">
  <h1 class="abs">Richer Data To Drive Your Business</h1>
  <p class="lead abs">Korvane makes it easy to derive data for the businesses to make it more efficient.</p>
  <a class="btn btn-ghost abs" style="left:524px;top:212px;width:151px;height:46px">Free Trail &nbsp;→</a>
</section>
<svg class="hero-curve abs" width="1200" height="40" viewBox="0 0 1200 40"><path d="M0 0 L600 36 L1200 0 V40 H0z" fill="#fff"/></svg>
<div class="hero-card abs" style="left:150px;top:448px;width:404px;height:227px">
  <h2>Comprehensive Company Information</h2>
  <a class="btn btn-white abs" style="left:128px;top:101px;width:150px;height:44px;font-weight:700">Company API</a>
</div>
<div class="hero-card abs" style="left:645px;top:508px;width:405px;height:167px;padding:26px 57px">
  <h2>Bring Mapping Data into Your Business</h2>
  <a class="btn btn-ghost abs" style="left:128px;top:101px;width:150px;height:44px;background:var(--navy-deep)">Location API</a>
</div>

<section class="who">
  <div class="rule abs" style="left:150px;top:735px"></div>
  <h2 class="abs" style="left:150px;top:750px">Who are we ?</h2>
  <div class="abs" style="left:150px;top:811px;width:451px">
    <p>Korvane is setup for connected world. A world where data is integrated,comprehensive and useful. Where systems are designed to cooperate to make business more efficient. For this purpose we have focused on two key areas of work-location and company data.</p>
    <p>Our <u>Postal API</u> is the most current in the marketplace, helping anyone pinpoint a map simply by providing a postcode. This allows you to assign a loction to your postal-level business data. We also provide an <u>Address API</u>, giving you address for any postcode along with it's coordinate on the ground. We also supply base maps for customers looking to use maps on their website. And we supply a wide range pf <u>bespoke GIS services</u> for more specific mapping work.</p>
  </div>
  <a class="btn btn-solid abs" style="left:150px;top:1081px;width:112px;height:45px">Read More</a>
  <div class="illustration abs" role="img" aria-label="Illustration of data reports with charts, a magnifying glass, glasses and a calculator"></div>
</section>

<section class="services abs" role="img" aria-label="Deep blue sea surface background">
  <div class="rule abs" style="left:152px;top:30px;background:#fff"></div>
  <h2 class="abs">Our Services</h2>

  <div class="service-card abs" style="top:110px">
    <h3><svg width="30" height="28" viewBox="0 0 30 28" fill="none" stroke="#fff" stroke-width="1.5"><rect x="3" y="6" width="24" height="21"/><rect x="10" y="1" width="10" height="5"/><path d="M7 11h3M13 11h4M20 11h3M7 16h3M13 16h4M20 16h3M12 27v-6h6v6"/></svg>Company API</h3>
    <p>Your supply one or more company numbers - we<br>send back everything via a simple API or CSV file</p>
    <a class="btn btn-white abs" style="left:162px;top:167px;width:180px;height:46px">Find out more</a>
    <a class="btn btn-ghost abs" style="left:372px;top:167px;width:180px;height:46px;background:var(--navy-deep)">Free Trail</a>
    <div class="badge abs">
      <svg width="80" height="80" viewBox="0 0 80 80"><polygon points="40,2 50,10 63,8 67,20 78,28 73,40 78,52 67,60 63,72 50,70 40,78 30,70 17,72 13,60 2,52 7,40 2,28 13,20 17,8 30,10" fill="none" stroke="#fff" stroke-width="2.5"/></svg>
      <span style="top:15px;font-size:10px;font-weight:700">From</span>
      <span style="top:24px;font-size:25px">£29</span>
      <span style="top:56px;font-size:10px;font-weight:700">only</span>
    </div>
  </div>

  <div class="service-card abs" style="top:398px">
    <h3><svg width="22" height="28" viewBox="0 0 22 28"><path fill="#fff" d="M11 0a11 11 0 00-11 11c0 8 11 17 11 17s11-9 11-17A11 11 0 0011 0zm0 15a4 4 0 110-8 4 4 0 010 8z"/></svg>Location API</h3>
    <p>You send us a postcode, we send you the location. Or you<br>send us the location, we send back the postcode: API or CSV</p>
    <a class="btn btn-white abs" style="left:162px;top:168px;width:180px;height:46px">Find out more</a>
    <a class="btn btn-ghost abs" style="left:372px;top:168px;width:180px;height:46px;background:var(--navy-deep)">Free Trail</a>
    <div class="badge abs">
      <svg width="80" height="80" viewBox="0 0 80 80"><polygon points="40,2 50,10 63,8 67,20 78,28 73,40 78,52 67,60 63,72 50,70 40,78 30,70 17,72 13,60 2,52 7,40 2,28 13,20 17,8 30,10" fill="none" stroke="#fff" stroke-width="2.5"/></svg>
      <span style="top:15px;font-size:10px;font-weight:700">From</span>
      <span style="top:24px;font-size:25px">£29</span>
      <span style="top:56px;font-size:10px;font-weight:700">only</span>
    </div>
  </div>
</section>
<svg class="abs" style="left:0;top:1874px" width="1200" height="41" viewBox="0 0 1200 41"><path d="M0 0 L600 40 L1200 0 V41 H0z" fill="#fff"/></svg>

<section class="cta">
  <h2 class="abs">Go Ahead: Test our Data; or let's talk it through</h2>
  <p class="abs">If you are confident you know what you want, why not start a trial? It's free of charge and you can test the service for a limited time. If you are not sure or you have a very specific requirements then talk to our consultants.</p>
  <a class="btn btn-solid abs" style="left:405px;top:2118px;width:180px;height:44px;font-weight:400">Call (+44) 01632 960 214</a>
  <a class="btn btn-outline abs" style="left:615px;top:2118px;width:180px;height:44px">Send an email</a>
</section>
<div class="divider abs"></div>

<section class="demand">
  <div class="photo abs" role="img" aria-label="Photo of two developers working at laptops in a dim office"></div>
  <h2 class="abs">Demanding Data Requirements? Look No Further</h2>
  <div class="body abs">
    <p>Most business looking for our help have complex data requirements they need to piece together. It may be they have an in-house team, but if not, we can help with:</p>
    <ul>
      <li>Connecting our API into existing systems and software</li>
      <li>Helping with more complex business or loction data supply</li>
      <li>Placing experienced staff on site to assist with mapping and data projects</li>
      <li>Helping businesses automate and digitally transform</li>
    </ul>
    <p style="margin-top:16px">So if you want us to help you take your integration up a notch, then let's talk. Please call <b>(+44) 01632 960 214</b> or</p>
  </div>
  <a class="btn btn-solid abs" style="left:870px;top:2516px;width:180px;height:44px;font-weight:400">Bespoke Services</a>
</section>

<section>
  <div class="map abs" role="img" aria-label="Street map of the area around the office with a location pin"></div>
  <svg class="abs" style="left:632px;top:2755px" width="24" height="32" viewBox="0 0 22 28"><path fill="#e53935" d="M11 0a11 11 0 00-11 11c0 8 11 17 11 17s11-9 11-17A11 11 0 0011 0zm0 15a4 4 0 110-8 4 4 0 010 8z"/></svg>
  <div class="loc-panel abs">
    <h2>Where is Korvane?</h2>
    <address>Second Floor, 12 Marlow Yard<br>Wexcombe Park<br>Harwell<br>Reading RG4 2XT<br>Contact: (+44) 01632 960 214</address>
    <a class="btn btn-white abs" style="left:112px;top:300px;width:179px;height:44px">Send an email</a>
  </div>
</section>

<footer class="footer abs">
  <div class="foot-col abs" style="left:150px"><h4>Company Data</h4><a>Company Information</a><a>Alerts and Notifications</a><a>Contact Information</a><a>Financial Information</a><a>Other Data Services</a></div>
  <div class="foot-col abs" style="left:424px;top:79px"><h4>Location Data</h4><a>Postal Lookup</a><a>Address Lookup</a><a>Base Mapping</a><a>Boundaries</a><a>Bespoke Mapping</a></div>
  <div class="foot-col abs" style="left:700px;top:79px"><h4>Services</h4><a>API/Integration</a><a>Licensing/IPR</a><a>Complex Location Data</a><a>Digital Transformation</a></div>
  <div class="foot-col abs" style="left:975px"><h4>Korvane</h4><a>Pricing</a><a>About Us</a><a>Contact Us</a><a>Free Trail</a><a>Login</a></div>
  <div class="legal abs">Linnet Digital Limited 2019 © All rights reserved
    <nav><a>Sitemap</a><a>Terms of UsePrivacy</a><a>Policy</a><a>ContactUs</a></nav>
  </div>
</footer>

</body>
</html>
```